Tech business card design

We need an amazing business card design for our new business 'Brakka' a marketing tech startup based in Sydney, Australia. We provide an online marketplace for businesses to search and buy advertising media, connect with service providers and learn more about marketing. We wish to communicate 'cool tech', reliability and professionalism and design based around our logo.

Target Market(s)

Business Owners

Contact Information for Business Card

Name
Position
Email Address
Website
Phone Number

Font styles to use
Other font styles liked:
• Avenir & Avenir Next

Colors

Designer to choose colors to be used in the design.

```html
<!DOCTYPE html>
<html lang="en">
<head>
<meta charset="utf-8">
<title>Brakka business card</title>
<link rel="stylesheet" href="https://fonts.googleapis.com/css2?family=Nunito+Sans:wght@400;600;800&display=swap">
<style>
  :root {
    --stage-light: #e6e7e9;
    --stage-dark: #c9cacc;
    --card-blue: #2e3192;
    --glow-cyan: #3fb6e6;
    --glow-blue: #2a6fd0;
    --ink-white: #ffffff;
    --ink-soft: #e8ebff;
  }
  * { margin: 0; padding: 0; box-sizing: border-box; }
  html, body { width: 800px; height: 1200px; overflow: hidden; }
  body {
    position: relative;
    background: radial-gradient(ellipse at 50% 45%, var(--stage-light) 0%, var(--stage-dark) 100%);
    font-family: "Nunito Sans", "Avenir Next", Avenir, sans-serif;
    color: var(--ink-white);
  }
  .card {
    position: absolute;
    left: 148px;
    width: 504px;
    height: 288px;
    background: var(--card-blue);
    overflow: hidden;
  }
  .card--front { top: 156px; }
  .card--back { top: 692px; }

  .network-art { position: absolute; inset: 0; }
  .card--front .network-art {
    background:
      radial-gradient(circle at 58px 186px, rgba(63,182,230,0.85) 0%, rgba(42,111,208,0.55) 28%, rgba(46,49,146,0) 62%),
      radial-gradient(circle at 8px 120px, rgba(63,182,230,0.6) 0%, rgba(46,49,146,0) 40%);
  }
  .card--back .network-art {
    background:
      radial-gradient(circle at 460px 240px, rgba(63,182,230,0.9) 0%, rgba(42,111,208,0.55) 26%, rgba(46,49,146,0) 58%),
      radial-gradient(circle at 70px 250px, rgba(42,111,208,0.35) 0%, rgba(46,49,146,0) 30%);
  }

  .brand-name {
    position: absolute;
    font-weight: 800;
    letter-spacing: -1px;
    line-height: 1;
    color: var(--ink-white);
  }
  .card--front .brand-name { left: 294px; top: 34px; font-size: 52px; }
  .card--back .brand-name { left: 30px; top: 24px; font-size: 68px; }

  .contact-block { position: absolute; left: 294px; top: 119px; }
  .person-name { font-size: 25px; font-weight: 600; line-height: 1; }
  .person-role { font-size: 14.5px; font-weight: 400; color: var(--ink-soft); margin-top: 2px; }
  .contact-list { list-style: none; margin-top: 17px; }
  .contact-list li {
    display: flex; align-items: center;
    font-size: 15px; line-height: 24.5px;
    color: var(--ink-soft);
  }
  .contact-icon { width: 9px; height: 9px; margin-right: 7px; flex: none; }
</style>
</head>
<body>
  <section class="card card--front">
    <div class="network-art" role="img" aria-label="Glowing constellation network of connected points and thin lines on the left"></div>
    <div class="brand-name">Brakka</div>
    <div class="contact-block">
      <div class="person-name">Dana Reyes</div>
      <div class="person-role">Managing Director</div>
      <ul class="contact-list">
        <li>
          <svg class="contact-icon" viewBox="0 0 10 10" aria-hidden="true"><path d="M2.2 0.8 L3.8 2.6 L3 3.6 Q4 5.8 6.4 7 L7.4 6.2 L9.2 7.8 L8 9.3 Q3 8.6 0.8 2 Z" fill="#fff"/></svg>
          0123-456-789
        </li>
        <li>
          <svg class="contact-icon" viewBox="0 0 10 10" aria-hidden="true"><rect x="0.5" y="2" width="9" height="6.5" fill="#fff"/><path d="M0.5 2 L5 5.6 L9.5 2" fill="none" stroke="#2e3192" stroke-width="0.9"/></svg>
          Info@youremail.com
        </li>
        <li>
          <svg class="contact-icon" viewBox="0 0 10 10" aria-hidden="true"><circle cx="5" cy="5" r="4.5" fill="#fff"/><path d="M0.5 5 H9.5 M5 0.5 V9.5 M5 0.5 Q2 5 5 9.5 M5 0.5 Q8 5 5 9.5" fill="none" stroke="#2e3192" stroke-width="0.7"/></svg>
          www.yourweb.com
        </li>
      </ul>
    </div>
  </section>

  <section class="card card--back">
    <div class="network-art" role="img" aria-label="Glowing constellation network of connected points and thin lines across the lower right"></div>
    <div class="brand-name">Brakka</div>
  </section>
</body>
</html>
```